Dorrish Electric Ltd

Looking for a single page website and Facebook page design. I am an electrical contractor based on Vancouver Island. I do service, custom homes, residential and commercial installations. My company just started out, so I don't have any pictures of installs yet. I have 25 years experience. I would like the colors to be my logo colors black and I have a black Corvan Ridgeback that will be my vehicle which I will have a wrap for.
Updates

I just posted the contest today, not sure why the deadline is the same day.

Went on vacation/holiday

Industry/Entity Type

Electrician

Requirements
Must have
• Services provided, About me section, quote section,
Nice to have
• I am not quite sure yet, I need to see some designs first .

```html
<!DOCTYPE html>
<html lang="en">
<head>
<meta charset="utf-8">
<title>Dorrish Electric Ltd</title>
<link rel="stylesheet" href="https://fonts.googleapis.com/css2?family=Montserrat:wght@600&display=swap">
<style>
  :root {
    --paper: #fefefe;
    --ink: #000000;
    --volt: #f2b908;
    --light: #ffffff;
  }
  html, body {
    margin: 0;
    padding: 0;
    width: 1200px;
    height: 1200px;
    overflow: hidden;
    background: var(--paper);
  }
  .canvas {
    position: relative;
    width: 1200px;
    height: 1200px;
  }
  .banner {
    position: absolute;
    inset: 0;
  }
  .banner-ground { fill: var(--ink); }
  .banner-accent { fill: var(--volt); }
  .brand-mark {
    fill: none;
    stroke: var(--volt);
    stroke-width: 12;
  }
  .brand-name {
    position: absolute;
    left: 0;
    width: 1200px;
    top: 700px;
    margin: 0;
    text-align: center;
    font-family: "Montserrat", sans-serif;
    font-weight: 600;
    font-size: 39px;
    line-height: 1;
    letter-spacing: 1px;
    color: var(--light);
  }
</style>
</head>
<body>
<main class="canvas">
  <svg class="banner" width="1200" height="1200" viewBox="0 0 1200 1200" aria-hidden="true">
    <rect class="banner-ground" x="66" y="366" width="1068" height="468"/>
    <polygon class="banner-accent" points="66,596 319,366 206,834 66,834"/>
    <polygon class="banner-accent" points="879,564 1096,366 1134,366 1134,682 946,834"/>
    <circle class="brand-mark" cx="600" cy="565" r="100"/>
  </svg>
  <h1 class="brand-name">Dorrish Electric Ltd</h1>
</main>
</body>
</html>
```